bryn calvo website design

An IT support and IT Security Company - just use dummy text for now for the design. Examples of sites we like the looks and feel of but need it more professional feel are like: www.quorvatech.uk.com , www.halvion.co.uk, www.truvexa.com/professional/, www.zul.com, www.mivlen.com,

Best to message me if you have any questions

Target Market(s)

small to medium UK based companies that require IT support services

Industry/Entity Type

It Company

Contact Information for Business Card

use dummy name, telephone and email for now, will provide details later.

Logo Text

bryn calvo (and then below the logo it should say "your IT, networks and security partner")

Coding

Coded - Design and coding required

Number of Pages Required

5+ page

Colors

Designer to choose colors to be used in the design.

Requirements
Must have
• must be professional, yet simple and clear that this is a serious IT support and IT security company.
Nice to have
• 1)The website homepage must have professional quality pictures of IT support or London city skyline or any picture that projects friendly business partners, professionalism and ready to serve.
• 2) Home page needs to include tabs for following pages 'Services' , 'About Us' , 'Contact Us' 'Home'
• 3) Website built customised using wordpress is ideal and easy for us to manage.
• more room for boxed options from homepage (with pic or image in background)
Should not have
• no checkout trolleys or payment options.

```html
<!DOCTYPE html>
<html lang="en">
<head>
<meta charset="utf-8">
<title>Bryn Calvo – IT Support</title>
<link rel="stylesheet" href="https://fonts.googleapis.com/css2?family=Mulish:wght@400;600;700&family=Lato:wght@400;700&display=swap">
<style>
:root{
  --teal:#5ccdb8;
  --blue:#6a93de;
  --pink:#f27b8a;
  --ink:#1f1f1f;
  --muted:#6d6d6d;
  --pale:#f6f6f6;
  --white:#ffffff;
  --dark:#2b2b2b;
}
*{box-sizing:border-box;margin:0;padding:0}
html,body{width:1200px;height:2335px;overflow:hidden}
body{position:relative;background:var(--pale);font-family:"Lato",sans-serif;color:var(--ink)}
.abs{position:absolute}

/* header */
.brand{left:162px;top:14px;font-family:"Mulish",sans-serif;font-weight:700;font-size:31px;line-height:36px;color:var(--pink);letter-spacing:-.5px}
.tagline{left:163px;top:51px;font-family:"Mulish",sans-serif;font-weight:600;font-size:10px;line-height:13px;color:var(--muted);letter-spacing:.3px}
.top-links{right:160px;top:20px;display:flex;gap:6px}
.top-link{height:30px;padding:0 14px;display:flex;align-items:center;gap:6px;color:var(--white);font-size:12px;border-radius:3px}
.top-link.phone{background:var(--blue)}
.top-link.mail{background:var(--teal)}
.top-link.login{background:var(--blue)}
.main-nav{left:160px;top:72px;width:880px;height:40px;background:var(--teal);border-radius:3px;display:flex;align-items:center;padding-left:32px;gap:38px}
.main-nav a{color:var(--white);text-decoration:none;font-size:12px;font-family:"Mulish",sans-serif;font-weight:600;letter-spacing:.4px}

/* hero */
.hero{left:0;top:0;width:1200px;height:772px;background:var(--pale)}
.hero-photo{left:160px;top:121px;width:880px;height:475px;background:linear-gradient(120deg,#6b7480 0%,#9aa7b5 40%,#4d5866 75%,#2f3742 100%)}
.hero-band{left:160px;top:408px;width:880px;height:43px;background:rgba(40,45,55,.45);color:var(--white);font-family:"Mulish",sans-serif;font-size:30px;text-align:center;line-height:43px;letter-spacing:.5px}
.sector{width:268px;top:478px;height:205px;border-radius:6px;overflow:hidden;box-shadow:0 18px 24px -14px rgba(0,0,0,.25)}
.sector-head{height:45px;background:var(--white);text-align:center;line-height:45px;font-family:"Mulish",sans-serif;font-weight:600;font-size:14px}
.sector-body{height:160px;padding:16px 18px;color:var(--white)}
.sector-title{display:flex;align-items:center;gap:12px;font-size:12px;font-weight:700;font-family:"Mulish",sans-serif;line-height:15px;margin-bottom:10px}
.sector-text{font-size:10.5px;line-height:13px}
.sector-more{font-size:12px;font-weight:700;margin-top:14px}
.s-fin{left:176px}.s-fin .sector-head{color:var(--teal)}.s-fin .sector-body{background:var(--teal)}
.s-prop{left:465px}.s-prop .sector-head{color:var(--blue)}.s-prop .sector-body{background:var(--blue)}
.s-pro{left:755px}.s-pro .sector-head{color:var(--pink)}.s-pro .sector-body{background:var(--pink)}

/* about */
.about{left:0;top:772px;width:1200px;height:526px;background:var(--white)}
.num{font-family:"Mulish",sans-serif;font-size:11px;color:var(--teal);font-weight:700}
.num::after{content:"";display:block;width:34px;height:1px;background:var(--teal);margin-top:3px}
.sec-title{font-family:"Mulish",sans-serif;font-size:21px;font-weight:600;color:var(--ink);line-height:28px}
.rule{width:224px;height:2px;background:#e6e6e6}
.rule::before{content:"";display:block;width:72px;height:4px;margin-top:-1px;background:var(--blue)}
.about-photo{left:160px;top:194px;width:436px;height:260px;background:linear-gradient(135deg,#8c8f93,#d9d4cd 45%,#55585c)}
.checks{left:619px;top:198px;width:421px}
.check{display:flex;gap:12px;margin-bottom:22px}
.check h3{font-family:"Mulish",sans-serif;font-size:18px;font-weight:600;line-height:22px}
.check p{font-size:11.5px;color:var(--muted);margin-top:3px}
.help{left:627px;top:422px;font-size:13px;font-weight:600;color:var(--ink);font-family:"Mulish",sans-serif}
.call{left:811px;top:404px;width:182px;height:50px;background:var(--dark);color:var(--white);border-radius:3px;text-align:center;line-height:50px;font-size:13px;font-weight:700;font-family:"Mulish",sans-serif}

/* features */
.features{left:0;top:1298px;width:1200px;height:322px;background:var(--teal);color:var(--white)}
.feature{width:300px;text-align:center;top:43px}
.feature-icon{width:121px;height:106px;border:2px solid var(--white);border-radius:4px;margin:0 auto;display:flex;align-items:center;justify-content:center}
.feature h4{font-family:"Mulish",sans-serif;font-weight:400;font-size:14px;margin-top:34px;letter-spacing:.3px}
.feature p{font-size:11.5px;line-height:18px;margin-top:12px;padding:0 22px}

/* partners */
.partners-copy{left:160px;top:1675px;width:460px}
.lead{font-size:10.5px;font-weight:700;color:#555;margin-top:44px;letter-spacing:.1px;white-space:nowrap}
.body-text{font-size:12px;line-height:19px;color:#555;margin-top:6px;width:440px}
.learn{left:163px;top:1883px;width:181px;height:48px;background:var(--blue);color:var(--white);border-radius:2px;text-align:center;line-height:48px;font-size:13px;font-family:"Mulish",sans-serif}
.badge{background:#dfe2e8;border-radius:4px}

/* footer */
.footer{left:160px;top:1987px;width:880px;height:268px;background:var(--blue);color:var(--white)}
.f-col{top:46px}
.f-col h5{font-family:"Mulish",sans-serif;font-size:14px;font-weight:600;padding-bottom:8px;border-bottom:1px solid rgba(255,255,255,.9);display:inline-block;min-width:100px}
.f-row{display:flex;align-items:center;gap:10px;font-size:12px;margin-top:16px}
.f-row .lab{width:70px;color:#e7eeff}
.f-links{font-size:11px;line-height:20px;margin-top:14px}
.divider{top:30px;width:1px;height:206px;background:rgba(255,255,255,.7)}
.socials{display:flex;gap:6px;margin-top:18px}
.socials span{width:34px;height:34px;border:2px solid var(--white);border-radius:50%}
.copyright{left:160px;top:2273px;width:880px;font-size:11px;line-height:17px;color:#666}
</style>
</head>
<body>

<section class="hero abs">
  <div class="brand abs">Bryn Calvo</div>
  <div class="tagline abs">your IT, networks and security partner</div>
  <div class="top-links abs">
    <span class="top-link phone"><svg width="10" height="12" viewBox="0 0 10 12"><path d="M2 0 4 3 3 4.5Q4.5 7.5 6.5 8.5L8 7.5 10 10 8.5 12Q1 9 0 1Z" fill="#fff"/></svg>Toll Free : 001-555-0148</span>
    <span class="top-link mail"><svg width="12" height="9" viewBox="0 0 12 9"><rect width="12" height="9" fill="#fff"/><path d="M0 0 6 5 12 0" stroke="#5ccdb8" fill="none"/></svg>info@bryncalvo.uk</span>
    <span class="top-link login"><svg width="11" height="12" viewBox="0 0 11 12"><circle cx="5.5" cy="3.5" r="3" fill="none" stroke="#fff" stroke-width="1.4"/><path d="M.8 12Q1 7 5.5 7T10.2 12" fill="none" stroke="#fff" stroke-width="1.4"/></svg>LOGIN</span>
  </div>
  <nav class="main-nav abs">
    <a href="#">HOME</a><a href="#">ABOUT US</a><a href="#">BRYN CALVO SERVICES</a><a href="#">BLOG</a><a href="#">CONTACT US</a>
  </nav>
  <div class="hero-photo abs" role="img" aria-label="Hand with a pen over a laptop keyboard with a network diagram overlay"></div>
  <div class="hero-band abs">IT SUPPORT FOR</div>

  <article class="sector s-fin abs">
    <div class="sector-head">FINANCIAL SERVICES</div>
    <div class="sector-body">
      <div class="sector-title"><svg width="22" height="26" viewBox="0 0 22 26" fill="#fff"><rect x="1" y="16" width="4" height="10"/><rect x="7" y="12" width="4" height="14"/><rect x="13" y="8" width="4" height="18"/><text x="3" y="9" font-size="10" font-family="Lato" font-weight="700">$</text></svg>IT SUPPORT FOR FINANCIAL</div>
      <p class="sector-text">Lorem ipsum dolor sit amet, consectetur adipiscing elit, sed do eiusmod tempor incididunt ut labore et dolore magna aliqua.</p>
      <p class="sector-more">More Info</p>
    </div>
  </article>
  <article class="sector s-prop abs">
    <div class="sector-head">THE PROPERTY INDUSTRY</div>
    <div class="sector-body">
      <div class="sector-title"><svg width="24" height="28" viewBox="0 0 24 28" fill="#fff"><rect x="2" y="6" width="10" height="22"/><rect x="13" y="12" width="9" height="16"/><path d="M2 6 7 1 12 6Z"/></svg>IT SUPPORT FOR THE<br>PROPERTY INDUSTRY</div>
      <p class="sector-text">Lorem ipsum dolor sit amet, consectetur adipiscing elit, sed do eiusmod tempor incididunt ut labore et dolore magna aliqua.</p>
      <p class="sector-more">More Info</p>
    </div>
  </article>
  <article class="sector s-pro abs">
    <div class="sector-head">PROFESSIONAL SERVICES</div>
    <div class="sector-body">
      <div class="sector-title"><svg width="26" height="26" viewBox="0 0 26 26" fill="#fff"><path d="M4 22 6 15 19 2 24 7 11 20Z"/></svg>IT SUPPORT FOR PROFES-<br>SIONAL SERVICES</div>
      <p class="sector-text">Lorem ipsum dolor sit amet, consectetur adipiscing elit, sed do eiusmod tempor incididunt ut labore et dolore magna aliqua.</p>
      <p class="sector-more">More Info</p>
    </div>
  </article>
</section>

<section class="about abs">
  <div class="abs" style="left:160px;top:62px">
    <div class="num">01</div>
    <h2 class="sec-title" style="margin-top:6px">BRYN CALVO.UK<br>Lorem ipsum dolor sit amet,</h2>
    <div class="rule" style="margin-top:12px"></div>
  </div>
  <div class="about-photo abs" role="img" aria-label="Person writing on a tablet beside a laptop"></div>
  <div class="checks abs">
    <div class="check"><svg width="20" height="20" viewBox="0 0 20 20"><circle cx="10" cy="10" r="8.5" fill="none" stroke="#2a3f7a" stroke-width="2"/><path d="M6 10 9 13 14 7" fill="none" stroke="#2a3f7a" stroke-width="2"/></svg><div><h3>Lorem ipsum dolor sit amet.</h3><p>sed do eiusmod tempor incididunt ut labore et dolore magna aliqua.</p></div></div>
    <div class="check"><svg width="20" height="20" viewBox="0 0 20 20"><circle cx="10" cy="10" r="8.5" fill="none" stroke="#2a3f7a" stroke-width="2"/><path d="M6 10 9 13 14 7" fill="none" stroke="#2a3f7a" stroke-width="2"/></svg><div><h3>Lorem ipsum dolor sit amet.</h3><p>sed do eiusmod tempor incididunt ut labore et dolore magna aliqua.</p></div></div>
    <div class="check"><svg width="20" height="20" viewBox="0 0 20 20"><circle cx="10" cy="10" r="8.5" fill="none" stroke="#2a3f7a" stroke-width="2"/><path d="M6 10 9 13 14 7" fill="none" stroke="#2a3f7a" stroke-width="2"/></svg><div><h3>Lorem ipsum dolor sit amet.</h3><p>sed do eiusmod tempor incididunt ut labore et dolore magna aliqua.</p></div></div>
  </div>
  <div class="help abs">For Help or More Info</div>
  <div class="call abs">CALL : 001 - 555 - 0148</div>
</section>

<section class="features abs">
  <div class="feature abs" style="left:133px">
    <div class="feature-icon"><svg width="64" height="64" viewBox="0 0 64 64" fill="none" stroke="#fff" stroke-width="4"><circle cx="26" cy="26" r="16"/><path d="M38 38 56 56" stroke-width="8" stroke-linecap="round"/><circle cx="42" cy="14" r="5" stroke-width="3"/></svg></div>
    <h4>UT ENIM AD MINIM VENIAM,</h4>
    <p>Duis aute irure dolor in reprehenderit in voluptate velit esse cillum Ut enim ad minim veniam, quis nostrud exercitation ullamco laboris nisi ut aliquip ex ea commodo consequat.</p>
  </div>
  <div class="feature abs" style="left:448px">
    <div class="feature-icon"><svg width="64" height="60" viewBox="0 0 64 60" fill="none" stroke="#fff" stroke-width="3.5"><rect x="6" y="8" width="52" height="34"/><path d="M26 50h12M32 42v8M18 54h28"/><path d="M22 34 40 16 44 20 26 38 20 38Z" fill="#fff"/></svg></div>
    <h4>UT ENIM AD MINIM VENIAM,</h4>
    <p>Ut enim ad minim veniam, quis nostrud exercitation ullamco laboris nisi ut aliquip ex ea commodo consequat. Duis aute irure dolor in reprehenderit in voluptate.</p>
  </div>
  <div class="feature abs" style="left:773px">
    <div class="feature-icon"><svg width="64" height="64" viewBox="0 0 64 64" fill="none" stroke="#fff" stroke-width="4"><circle cx="26" cy="28" r="16"/><path d="M38 40 54 56" stroke-width="8" stroke-linecap="round"/><path d="M16 34 24 26 30 30 44 14M38 14h6v6"/></svg></div>
    <h4>UT ENIM AD MINIM VENIAM,</h4>
    <p>Quis nostrud exercitation ullamco laboris nisi ut aliquip ex ea commodo consequat. Duis aute irure dolor in reprehenderit in voluptate velit esse cillum</p>
  </div>
</section>

<section class="partners">
  <div class="partners-copy abs">
    <div class="num">02</div>
    <h2 class="sec-title" style="margin-top:6px">OUR BEST PARTNERS</h2>
    <div class="rule" style="margin-top:10px"></div>
    <p class="lead">LOREM IPSUM DOLOR SIT AMET, CONSECTETUR ADIPISCING ELIT, SED DO EIUSMOD</p>
    <p class="body-text">Ut enim ad minim veniam, quis nostrud exercitation ullamco laboris nisi ut aliquip ex ea commodo consequat. Duis aute irure dolor in reprehenderit in voluptate velit esse cillum dolore eu fugiat nulla pariatur.</p>
  </div>
  <div class="learn abs">LEARN MORE</div>
  <div class="badge abs" style="left:676px;top:1712px;width:150px;height:34px"></div>
  <div class="badge abs" style="left:888px;top:1712px;width:152px;height:34px"></div>
  <div class="badge abs" style="left:676px;top:1794px;width:118px;height:40px"></div>
  <div class="badge abs" style="left:824px;top:1800px;width:108px;height:28px"></div>
  <div class="badge abs" style="left:962px;top:1798px;width:78px;height:32px"></div>
  <div class="badge abs" style="left:676px;top:1884px;width:118px;height:30px"></div>
  <div class="badge abs" style="left:820px;top:1880px;width:122px;height:36px"></div>
  <div class="badge abs" style="left:964px;top:1886px;width:76px;height:26px"></div>
</section>

<footer class="footer abs">
  <div class="f-col abs" style="left:64px">
    <h5>Contact us</h5>
    <div class="f-row"><svg width="14" height="18" viewBox="0 0 14 18"><path d="M7 18Q0 9 0 7A7 7 0 0 1 14 7Q14 9 7 18Z" fill="#fff"/><circle cx="7" cy="7" r="2.5" fill="#6a93de"/></svg><span class="lab">Address :</span>Excepteur sint occaecat</div>
    <div class="f-row"><svg width="16" height="14" viewBox="0 0 16 14"><path d="M1 4Q8-1 15 4L13 6 11 4H5L3 6Z M3 7H13L15 13H1Z" fill="#fff"/></svg><span class="lab">Phone :</span>012-555-0193</div>
    <div class="f-row"><svg width="16" height="14" viewBox="0 0 16 14"><rect y="3" width="16" height="11" fill="#fff"/><rect x="4" width="8" height="5" fill="#fff" stroke="#6a93de"/></svg><span class="lab">Fax :</span>012-555-0193</div>
    <div class="f-row"><svg width="16" height="12" viewBox="0 0 16 12"><rect width="16" height="12" fill="#fff"/><path d="M0 0 8 7 16 0" stroke="#6a93de" fill="none"/></svg><span class="lab">Email :</span>info@bryncalvo.co.uk</div>
  </div>
  <div class="divider abs" style="left:365px"></div>
  <div class="f-col abs" style="left:412px">
    <h5>Navigation</h5>
    <div class="f-links">Home<br>About Us<br>Services<br>Contact Us</div>
  </div>
  <div class="divider abs" style="left:593px"></div>
  <div class="f-col abs" style="left:636px">
    <h5 style="border:none;padding-bottom:0">Follow Us</h5>
    <div class="socials"><span></span><span></span><span></span><span></span></div>
  </div>
</footer>

<p class="copyright abs">Copyrights ©2018 Bryn Calvo.uk Allrights are Reserved &nbsp;|&nbsp; Terms &amp; Condition &nbsp;|&nbsp; Privacy Policy &nbsp;|&nbsp; Lorem ipsum dolor sit amet, consectetur adipiscing elit, sed do eiusmod tempor incididunt ut labore et dolore magna aliqua.</p>

</body>
</html>
```